Meridian Groundworks
Project: Construction Stationery
Construction Stationery - Construction
Construction Stationery
Professional
Eng. Samir Qutub
Construction Manager
P.O.Box: 4706 Jeddah 23857 Palm Orchard Street Saudi Arabia Phone: +966 12 4870391 info@meridiangroundworks.example
info@meridiangroundworks.example
www.meridiangroundworks.example
Please don't submit business card solo, submit the following at once:- 1. Business card 2. Letterhead A 3. Letterhead B 4. Envelope 5. Notepad 6. Folder
Design
kelvorunt kelvorunt
Please don't submit business card solo, I don't need all stationery i need only what's mentioned in additional comments section in the brief. Please check attached logo.

```html
<!DOCTYPE html>
<html lang="en">
<head>
<meta charset="utf-8">
<title>Meridian Groundworks — Construction Stationery</title>
<link rel="stylesheet" href="https://fonts.googleapis.com/css2?family=Montserrat:wght@700&family=Open+Sans:wght@400;600&display=swap">
<style>
  :root {
    --backdrop: #e8e9eb;
    --paper: #ffffff;
    --brand-blue: #2356b8;
    --deep-blue: #163f93;
    --mid-blue: #3a6fd0;
    --accent-orange: #f29a1f;
    --ink: #555a66;
    --shadow: 0 2px 8px rgba(0,0,0,0.18);
    --band: linear-gradient(172deg, #f2a23a 0%, #3a6fd0 24%, #163f93 100%);
  }
  * { margin: 0; padding: 0; box-sizing: border-box; }
  html, body { width: 1200px; height: 936px; overflow: hidden; background: var(--backdrop); }
  body { position: relative; font-family: "Open Sans", Arial, sans-serif; color: var(--ink); }

  .sheet { position: absolute; background: var(--paper); box-shadow: var(--shadow); overflow: hidden; }
  .accent-band { position: absolute; left: 0; right: 0; bottom: 0; background: var(--band); }

  .brand { display: flex; align-items: center; gap: 6px; position: absolute; z-index: 1; }
  .brand-dot { border-radius: 50%; background: var(--brand-blue); flex: none; }
  .brand-name { font-family: "Montserrat", Arial, sans-serif; font-weight: 700; color: var(--brand-blue); text-transform: uppercase; line-height: 1.05; letter-spacing: 0.5px; }

  /* Letterhead */
  .letterhead { left: 183px; top: 33px; width: 395px; height: 685px; }
  .letterhead .brand { left: 22px; top: 24px; }
  .letterhead .brand-dot { width: 18px; height: 18px; }
  .letterhead .brand-name { font-size: 10px; }
  .letterhead .accent-band { height: 190px; }
  .letter-body { position: absolute; left: 22px; top: 118px; width: 300px; font-size: 5.4px; line-height: 1.6; }
  .letter-body p { margin-bottom: 9px; }
  .signature { width: 46px; height: 14px; background: linear-gradient(90deg, #c9ccd3, #e3e5ea); border-radius: 6px; margin: 6px 0 4px; }
  .letter-contact { position: absolute; left: 250px; top: 540px; width: 130px; font-size: 5.2px; line-height: 1.7; color: #fff; z-index: 1; }

  /* Folder */
  .folder { left: 634px; top: 33px; width: 457px; height: 685px; }
  .folder .brand { left: 0; right: 0; top: 236px; flex-direction: column; gap: 12px; }
  .folder .brand-dot { width: 58px; height: 58px; }
  .folder .brand-name { font-size: 26px; text-align: center; letter-spacing: 1px; }
  .folder .accent-band { height: 240px; }
  .folder-web { position: absolute; left: 0; right: 0; bottom: 50px; text-align: center; color: #fff; font-size: 9px; letter-spacing: 2.5px; z-index: 1; }

  /* Business cards */
  .card { left: 41px; width: 203px; height: 76px; }
  .card-front { top: 741px; }
  .card-back { top: 838px; }
  .card .brand { left: 10px; top: 10px; }
  .card .brand-dot { width: 10px; height: 10px; }
  .card .brand-name { font-size: 5.5px; }
  .card-front .accent-band { left: auto; top: 0; width: 92px; }
  .card-person { position: absolute; left: 10px; top: 38px; font-size: 4.6px; line-height: 1.5; }
  .card-person strong { color: var(--brand-blue); font-weight: 600; font-size: 5.2px; }
  .card-contact { position: absolute; right: 7px; top: 40px; font-size: 4.2px; line-height: 1.5; color: #fff; text-align: right; z-index: 1; }
  .card-back .brand { left: 0; right: 0; top: 32px; justify-content: center; }

  /* Envelopes */
  .envelope { top: 751px; height: 162px; }
  .envelope-front { left: 264px; width: 358px; }
  .envelope-front .brand { left: 16px; top: 16px; }
  .envelope-front .brand-dot { width: 16px; height: 16px; }
  .envelope-front .brand-name { font-size: 9px; }
  .envelope-front .accent-band { height: 52px; }
  .envelope-web { position: absolute; left: 0; right: 0; bottom: 14px; text-align: center; color: #fff; font-size: 6px; letter-spacing: 1.8px; z-index: 1; }
  .envelope-back { left: 644px; width: 447px; background: var(--brand-blue); }
  .envelope-back .flap { position: absolute; left: 0; top: 0; width: 100%; height: 100%; }
  .envelope-back .envelope-web { top: 26px; bottom: auto; font-size: 8px; }
</style>
</head>
<body>

  <section class="sheet letterhead">
    <div class="brand"><span class="brand-dot"></span><span class="brand-name">Meridian<br>Groundworks</span></div>
    <div class="letter-body">
      <p>June 4, 2024</p>
      <p>Dear Client,<br>Site Office, Jeddah</p>
      <p>We are pleased to confirm the schedule for the foundation works at your site. Our team will mobilise equipment next week and begin excavation once permits are approved.</p>
      <p>Please review the attached drawings and confirm the access routes so that deliveries can proceed without delay.</p>
      <p>Should you require further details on costs, materials or timelines, our project office is available to assist you at any time during working hours.</p>
      <p>Sincerely,</p>
      <div class="signature" role="img" aria-label="Handwritten signature"></div>
      <p><strong>Eng. Samir Qutub</strong><br>Construction Manager</p>
    </div>
    <div class="accent-band" role="img" aria-label="Decorative blue and orange graphic"></div>
    <div class="letter-contact">
      P.O.Box: 4706 Jeddah 23857<br>Palm Orchard Street<br>Saudi Arabia<br>Phone: +966 12 4870391<br>info@meridiangroundworks.example<br>www.meridiangroundworks.example
    </div>
  </section>

  <section class="sheet folder">
    <div class="brand"><span class="brand-dot"></span><span class="brand-name">Meridian<br>Groundworks</span></div>
    <div class="accent-band" role="img" aria-label="Decorative blue and orange graphic"></div>
    <div class="folder-web">www.meridiangroundworks.example</div>
  </section>

  <section class="sheet card card-front">
    <div class="brand"><span class="brand-dot"></span><span class="brand-name">Meridian<br>Groundworks</span></div>
    <div class="accent-band" role="img" aria-label="Decorative blue and orange graphic"></div>
    <div class="card-person"><strong>Eng. Samir Qutub</strong><br>Construction Manager</div>
    <div class="card-contact">+966 12 4870391<br>info@meridiangroundworks.example<br>Jeddah, Saudi Arabia</div>
  </section>

  <section class="sheet card card-back">
    <div class="brand"><span class="brand-dot"></span><span class="brand-name">Meridian Groundworks</span></div>
  </section>

  <section class="sheet envelope envelope-front">
    <div class="brand"><span class="brand-dot"></span><span class="brand-name">Meridian<br>Groundworks</span></div>
    <div class="accent-band" role="img" aria-label="Decorative blue and orange graphic"></div>
    <div class="envelope-web">www.meridiangroundworks.example</div>
  </section>

  <section class="sheet envelope envelope-back">
    <svg class="flap" viewBox="0 0 447 162" width="447" height="162" aria-hidden="true">
      <path d="M0 62 L223 128 L447 62 L447 162 L0 162 Z" fill="#ffffff"/>
    </svg>
    <div class="envelope-web">www.meridiangroundworks.example</div>
  </section>

</body>
</html>
```